Law Firm Business Cards/Letterhead/Envelopes
Holloway Law Firm, PLLC Business Cards/Letterhead/Envelopes
I need double sided standard sized Business Card [3.5" x 2"]
Selective use of Same font as logo and also may use other type of font
Simple
Martin J. Holloway
Attorney & Counselor at Law
2650 Prairie Ridge Road - Suite 1200
Bloomington, MN 55429
martin@holfirm.example
www.holfirm.example
The front of the card I would like to incorporate my logo and firm name, my name, title, address, numbers/fax, email and website. The business card WILL NOT have curved corners. Open to different possibilities but dont want the card too busy....I'd prefer something on the "simple" side...Same goes for envelope and letterhead.
Probably just Logo, Firm name and address all in upper left of envelope.
Letterhead - Logo and firm name up top somewhere...address at bottom....do not include my name and my title on letterhead.
The back of the card I would like to only incorporate the Logo and website OR Logo and firm name and website. The business card WILL NOT have curved corners. Possibly a different color back (possibly grey), but not necessarily. Possibly a watermark of the logo used somewhere...open to different possibilities but dont want the card too busy....I'd prefer something on the "simple" side...
Logo to the Left
Folder Template

```html
<!DOCTYPE html>
<html lang="en">
<head>
<meta charset="utf-8">
<title>Holloway Law Firm, PLLC — Stationery</title>
<link href="https://fonts.googleapis.com/css2?family=Cinzel:wght@400;600&display=swap" rel="stylesheet">
<style>
  :root {
    --stage: #4a4a4c;
    --paper: #ffffff;
    --navy: #1d3f63;
    --navy-deep: #0f2740;
    --steel: #9aa3ad;
    --ink: #3a3d42;
    --charcoal: #2c2d30;
    --charcoal-light: #46484c;
    --flap: #5b5e63;
  }
  * { box-sizing: border-box; margin: 0; padding: 0; }
  html, body { width: 1200px; height: 1035px; overflow: hidden; }
  body { background: var(--stage); font-family: "Cinzel", serif; color: var(--ink); position: relative; }
  .piece { position: absolute; background: var(--paper); overflow: hidden; box-shadow: 0 4px 14px rgba(0,0,0,.35); }

  .mark { display: flex; align-items: center; gap: 10px; color: var(--navy); font-weight: 600; }
  .mark__box { width: 34px; height: 34px; background: var(--navy); flex: none; }
  .mark__name { line-height: 1; }
  .mark__firm { display: block; font-size: 30px; letter-spacing: 1px; }
  .mark__sub { display: block; font-size: 13px; letter-spacing: 3px; margin-top: 4px; }

  .address { font-size: 10px; line-height: 1.55; letter-spacing: .6px; text-transform: uppercase; color: var(--ink); }

  /* Letterhead */
  .letterhead { left: 90px; top: 55px; width: 555px; height: 755px; }
  .letterhead__bar { position: absolute; left: 28px; top: 0; width: 12px; height: 100%;
    background: linear-gradient(180deg, var(--navy-deep), var(--navy) 45%, #2f5f8e 70%, var(--navy-deep)); }
  .letterhead__chips { position: absolute; left: 0; top: 70px; width: 22px; }
  .letterhead__chips span { display: block; height: 14px; background: var(--steel); margin-bottom: 10px; }
  .letterhead__chips span:first-child { width: 22px; }
  .letterhead__chips span:nth-child(2) { width: 16px; }
  .letterhead__rule { position: absolute; left: 46px; top: 0; width: 2px; height: 100%; background: var(--steel); opacity: .5; }
  .letterhead .mark { position: absolute; left: 66px; top: 42px; }
  .letterhead .address { position: absolute; left: 66px; bottom: 32px; }

  /* Envelope back */
  .envelope-back { left: 660px; top: 70px; width: 465px; height: 320px; }
  .envelope-back svg { position: absolute; inset: 0; }
  .envelope-back__seal { position: absolute; left: 50%; top: 54px; width: 34px; height: 34px; margin-left: -17px; background: var(--navy); }
  .envelope-back__seal--lower { top: 248px; background: var(--paper); }

  /* Envelope front */
  .envelope-front { left: 660px; top: 420px; width: 465px; height: 210px; }
  .envelope-front__strip { position: absolute; left: 0; top: 0; width: 8px; height: 100%; background: var(--navy); }
  .envelope-front__strip--light { left: 11px; width: 3px; background: var(--steel); }
  .envelope-front .mark { position: absolute; left: 32px; top: 24px; }
  .envelope-front .mark__firm { font-size: 24px; }
  .envelope-front .mark__sub { font-size: 10px; }
  .envelope-front .mark__box { width: 28px; height: 28px; }
  .envelope-front .address { position: absolute; left: 32px; top: 160px; font-size: 9px; }

  /* Card: white front */
  .card-front { left: 660px; top: 650px; width: 290px; height: 160px; }
  .card-front__strip { position: absolute; left: 0; top: 0; width: 7px; height: 100%; background: var(--navy); }
  .card-front .mark { position: absolute; left: 112px; top: 18px; gap: 7px; }
  .card-front .mark__box { width: 20px; height: 20px; }
  .card-front .mark__firm { font-size: 17px; }
  .card-front .mark__sub { font-size: 7px; letter-spacing: 2px; margin-top: 2px; }
  .person { position: absolute; left: 24px; top: 70px; }
  .person__name { font-size: 10px; font-weight: 600; color: var(--navy); letter-spacing: .5px; }
  .person__title { font-size: 6.5px; letter-spacing: .8px; color: var(--ink); text-transform: uppercase; margin-top: 2px; }
  .card-front .contact { position: absolute; left: 24px; bottom: 16px; font-size: 6.5px; line-height: 1.6; letter-spacing: .4px; color: var(--ink); }

  /* Card: white back */
  .card-back { left: 660px; top: 830px; width: 290px; height: 175px; }
  .card-back__strip { position: absolute; left: 0; top: 0; width: 7px; height: 100%; background: var(--navy); }
  .card-back .mark { position: absolute; left: 42px; top: 58px; }
  .card-back .mark__box { width: 28px; height: 28px; }
  .card-back .mark__firm { font-size: 26px; }
  .card-back .mark__sub { font-size: 10px; }
  .card-back__web { position: absolute; left: 0; right: 0; bottom: 20px; text-align: center; font-size: 8px; letter-spacing: 1.5px; color: var(--ink); }

  /* Dark cards */
  .card-dark { top: 830px; height: 140px; background: linear-gradient(135deg, var(--charcoal-light), var(--charcoal)); color: #d8dce1; }
  .card-dark--front { left: 90px; width: 290px; }
  .card-dark--back { left: 392px; width: 253px; }
  .card-dark__bars { position: absolute; left: 0; top: 18px; width: 100%; }
  .card-dark__bars span { display: block; height: 5px; background: var(--steel); margin-bottom: 5px; opacity: .55; }
  .card-dark__bars span:nth-child(1) { width: 18px; }
  .card-dark__bars span:nth-child(2) { width: 12px; }
  .card-dark__stripe { position: absolute; left: 24px; top: 0; width: 5px; height: 100%; background: var(--navy); }
  .card-dark .mark { color: #d8dce1; gap: 7px; }
  .card-dark .mark__box { background: #d8dce1; width: 18px; height: 18px; }
  .card-dark .mark__firm { font-size: 15px; }
  .card-dark .mark__sub { font-size: 6.5px; letter-spacing: 2px; margin-top: 2px; }
  .card-dark--front .mark { position: absolute; left: 118px; top: 18px; }
  .card-dark--front .person { left: 40px; top: 66px; }
  .card-dark--front .person__name { color: #ffffff; }
  .card-dark--front .person__title { color: #b9c0c8; }
  .card-dark--front .contact { position: absolute; left: 40px; bottom: 14px; font-size: 6px; line-height: 1.6; letter-spacing: .4px; color: #b9c0c8; }
  .card-dark--back .watermark { position: absolute; left: 20px; top: 18px; width: 104px; height: 104px; background: #ffffff; opacity: .06; }
  .card-dark--back .mark { position: absolute; left: 40px; top: 58px; }
  .card-dark--back .mark__firm { font-size: 18px; }
  .card-dark--back .mark__sub { font-size: 7.5px; }
  .card-dark--back .web { position: absolute; left: 0; right: 0; bottom: 14px; text-align: center; font-size: 7px; letter-spacing: 1.5px; color: #b9c0c8; }
</style>
</head>
<body>

<section class="piece letterhead" aria-label="Letterhead">
  <div class="letterhead__chips"><span></span><span></span></div>
  <div class="letterhead__bar"></div>
  <div class="letterhead__rule"></div>
  <div class="mark">
    <span class="mark__box"></span>
    <span class="mark__name"><span class="mark__firm">HOLLOWAY</span><span class="mark__sub">LAW FIRM, PLLC</span></span>
  </div>
  <div class="address">
    2650 Prairie Ridge Road<br>
    Suite 1200, Bloomington, MN 55429<br>
    Toll free: (888) 555-0142<br>
    Phone: (952) 555-0187<br>
    Fax: (952) 555-0188<br>
    Email: martin@holfirm.example<br>
    Web: www.holfirm.example
  </div>
</section>

<section class="piece envelope-back" aria-label="Envelope back">
  <svg width="465" height="320" viewBox="0 0 465 320">
    <polygon points="0,0 465,0 232,140" fill="#f1f2f4" stroke="#d6d9dd"/>
    <line x1="0" y1="160" x2="465" y2="160" stroke="#d6d9dd"/>
    <polygon points="0,200 232,230 465,200 465,320 0,320" fill="#5b5e63"/>
    <polygon points="0,200 232,300 465,200 465,210 232,310 0,210" fill="#46484c"/>
  </svg>
  <div class="envelope-back__seal"></div>
  <div class="envelope-back__seal envelope-back__seal--lower"></div>
</section>

<section class="piece envelope-front" aria-label="Envelope front">
  <div class="envelope-front__strip"></div>
  <div class="envelope-front__strip envelope-front__strip--light"></div>
  <div class="mark">
    <span class="mark__box"></span>
    <span class="mark__name"><span class="mark__firm">HOLLOWAY</span><span class="mark__sub">LAW FIRM, PLLC</span></span>
  </div>
  <div class="address">
    2650 Prairie Ridge Road<br>
    Suite 1200, Bloomington, MN 55429
  </div>
</section>

<section class="piece card-front" aria-label="Business card front">
  <div class="card-front__strip"></div>
  <div class="mark">
    <span class="mark__box"></span>
    <span class="mark__name"><span class="mark__firm">HOLLOWAY</span><span class="mark__sub">LAW FIRM, PLLC</span></span>
  </div>
  <div class="person">
    <div class="person__name">Martin J. Holloway</div>
    <div class="person__title">Attorney &amp; Counselor at Law</div>
  </div>
  <div class="contact">
    2650 Prairie Ridge Road · Suite 1200 · Bloomington, MN 55429<br>
    Phone: (952) 555-0187 · Fax: (952) 555-0188<br>
    martin@holfirm.example · www.holfirm.example
  </div>
</section>

<section class="piece card-back" aria-label="Business card back">
  <div class="card-back__strip"></div>
  <div class="mark">
    <span class="mark__box"></span>
    <span class="mark__name"><span class="mark__firm">HOLLOWAY</span><span class="mark__sub">LAW FIRM, PLLC</span></span>
  </div>
  <div class="card-back__web">www.holfirm.example</div>
</section>

<section class="piece card-dark card-dark--front" aria-label="Business card front, grey version">
  <div class="card-dark__bars"><span></span><span></span></div>
  <div class="card-dark__stripe"></div>
  <div class="mark">
    <span class="mark__box"></span>
    <span class="mark__name"><span class="mark__firm">HOLLOWAY</span><span class="mark__sub">LAW FIRM, PLLC</span></span>
  </div>
  <div class="person">
    <div class="person__name">Martin J. Holloway</div>
    <div class="person__title">Attorney &amp; Counselor at Law</div>
  </div>
  <div class="contact">
    2650 Prairie Ridge Road · Suite 1200 · Bloomington, MN 55429<br>
    Phone: (952) 555-0187 · Fax: (952) 555-0188<br>
    martin@holfirm.example · www.holfirm.example
  </div>
</section>

<section class="piece card-dark card-dark--back" aria-label="Business card back, grey version">
  <div class="watermark"></div>
  <div class="mark">
    <span class="mark__box"></span>
    <span class="mark__name"><span class="mark__firm">HOLLOWAY</span><span class="mark__sub">LAW FIRM, PLLC</span></span>
  </div>
  <div class="web">www.holfirm.example</div>
</section>

</body>
</html>
```